Korvex Systems*

Stationary design including business cards, letter heads, envelops and email signatures using our new logo

Target Market(s)

Innovative Technologies

Industry/Entity Type

Defense Contracting

Font styles to use
Sans Serif

```html
<!DOCTYPE html>
<html lang="en">
<head>
<meta charset="utf-8">
<title>Korvex Systems — Business Card</title>
<link href="https://fonts.googleapis.com/css2?family=Roboto:wght@300;400;700&display=swap" rel="stylesheet">
<style>
  :root {
    --stage: #1c1c1d;
    --card-light: #ffffff;
    --card-dark: #262627;
    --ink: #111111;
    --ink-soft: #8a8a8a;
    --emboss: #3a3a3c;
    --emboss-edge: #444446;
  }
  * { margin: 0; padding: 0; box-sizing: border-box; }
  html, body {
    width: 1200px;
    height: 900px;
    overflow: hidden;
    background: var(--stage);
    font-family: "Roboto", Arial, sans-serif;
  }
  .stage {
    width: 1200px;
    height: 900px;
    display: flex;
    align-items: center;
    justify-content: center;
    gap: 80px;
  }
  .card {
    width: 350px;
    height: 600px;
    position: relative;
    box-shadow: 0 20px 40px rgba(0,0,0,0.55);
  }
  .card--front {
    background: var(--card-light);
    color: var(--ink);
    padding: 70px 44px 60px;
    display: flex;
    flex-direction: column;
  }
  .card--back {
    background: var(--card-dark);
    display: flex;
    align-items: center;
    justify-content: center;
  }
  .brand {
    display: flex;
    align-items: center;
    gap: 14px;
  }
  .brand__mark {
    width: 22px;
    height: 22px;
    background: var(--ink);
    flex: none;
  }
  .brand__name {
    font-weight: 300;
    font-size: 27px;
    letter-spacing: 1px;
    text-transform: uppercase;
    color: var(--ink);
  }
  .card--back .brand__mark { background: var(--emboss); }
  .card--back .brand__name {
    color: var(--emboss);
    font-size: 30px;
  }
  .person {
    margin-top: 190px;
  }
  .person__name {
    font-weight: 700;
    font-size: 21px;
  }
  .person__role {
    font-weight: 400;
    font-size: 15px;
    color: var(--ink-soft);
    margin-top: 4px;
  }
  .person__rule {
    width: 46px;
    height: 2px;
    background: var(--ink);
    margin-top: 10px;
  }
  .address {
    margin-top: 30px;
    font-size: 14px;
    font-weight: 300;
    color: var(--ink-soft);
    line-height: 1.45;
    font-style: normal;
  }
  .contact {
    list-style: none;
    margin-top: 14px;
    font-size: 14px;
    font-weight: 300;
    color: var(--ink-soft);
  }
  .contact__item {
    display: flex;
    align-items: center;
    gap: 9px;
    line-height: 1.5;
  }
  .contact__icon {
    width: 11px;
    height: 11px;
    flex: none;
  }
</style>
</head>
<body>
  <main class="stage">
    <section class="card card--front">
      <div class="brand">
        <span class="brand__mark"></span>
        <span class="brand__name">Korvex Systems</span>
      </div>

      <div class="person">
        <p class="person__name">Dana Whitcombe</p>
        <p class="person__role">Founder &amp; CEO</p>
        <div class="person__rule"></div>
      </div>

      <address class="address">
        48 Harbor Lane Suite 110<br>
        Riverton Address, Country
      </address>

      <ul class="contact">
        <li class="contact__item">
          <svg class="contact__icon" viewBox="0 0 24 24"><path fill="#111" d="M6.6 10.8a15.1 15.1 0 0 0 6.6 6.6l2.2-2.2c.3-.3.7-.4 1-.2 1.1.4 2.3.6 3.6.6.6 0 1 .4 1 1V20c0 .6-.4 1-1 1A17 17 0 0 1 3 4c0-.6.4-1 1-1h3.5c.6 0 1 .4 1 1 0 1.3.2 2.5.6 3.6.1.3 0 .7-.2 1z"/></svg>
          <span>+1 555.010.2040</span>
        </li>
        <li class="contact__item">
          <svg class="contact__icon" viewBox="0 0 24 24"><path fill="#111" d="M2 5h20v14H2z"/><path fill="none" stroke="#fff" stroke-width="2" d="M2 5l10 8 10-8"/></svg>
          <span>info@korvexsystems.com</span>
        </li>
        <li class="contact__item">
          <svg class="contact__icon" viewBox="0 0 24 24"><g fill="none" stroke="#111" stroke-width="2"><circle cx="12" cy="12" r="10"/><ellipse cx="12" cy="12" rx="4" ry="10"/><path d="M2 12h20"/></g></svg>
          <span>www.korvexsystems.com</span>
        </li>
      </ul>
    </section>

    <section class="card card--back">
      <div class="brand">
        <span class="brand__mark"></span>
        <span class="brand__name">Korvex Systems</span>
      </div>
    </section>
  </main>
</body>
</html>
```